qe road spares (www.qe-roadspares.net) needs a logo box design

we need to design 2 new box for same brand with colour and same design for our company which is specialist with auto parts to be produced in china, brake pads of same brand (Hyemin) the colour is Light blue or Azure and olive colour for lines the only difference between the boxes is the type which is brake pads or brake shoes only

below the logo it should be written Busan, Korea
(not made in)

all details are in the attached file

once you finish please send it as 2d and 3d pdf file

Target Market(s)

AUTO PARTS PARTS

Font styles to use
Script

Colors
33a6d7
add136

Requirements
Must have
• formula
logo
brand name
email: info@qe-roadspares.net
Nice to have
• LOGO ON THE BOX THAT STANDS FOR THE NAME OF THE BRAND
THE BRAND NAME
THE CITY OF PRODUCTION AND COUNTRY BUT WITHOUT WRITING MADE IN
THE FORMULA
SOME SAFETY RULES
ATTRACTIVE COLOURS AND DESIGNS
SOME LABELS AND ATTRACTIVE FEATURES
TAKE AS REFERENSE MORLAN BRAKE PADS BRAND

```html
<!DOCTYPE html>
<html lang="en">
<head>
<meta charset="utf-8">
<title>Hyemin Brake Pads – Box Dielines</title>
<link rel="stylesheet" href="https://fonts.googleapis.com/css2?family=Poppins:wght@400;500;600&display=swap">
<style>
  :root{
    --page:#d6e4f3;
    --navy:#0b2660;
    --azure:#33a6d7;
    --sky:#22b8e8;
    --deep:#1c62ae;
    --olive:#add136;
    --white:#ffffff;
    --cut:#8a8f96;
    --label:#e6007e;
  }
  html,body{margin:0;padding:0;overflow:hidden;background:var(--page);}
  .canvas{width:1200px;height:1200px;position:relative;overflow:hidden;background:var(--page);font-family:"Poppins",sans-serif;}
  .canvas svg{display:block;width:1200px;height:1200px;}
  .flap{fill:var(--white);stroke:var(--cut);stroke-width:1;}
  .panel-navy{fill:var(--navy);}
  .panel-sky{fill:var(--sky);}
  .stripe{fill:var(--olive);}
  .brand-mark{font-family:"Poppins",sans-serif;font-weight:600;fill:var(--olive);}
  .brand-city{font-family:"Poppins",sans-serif;font-weight:600;fill:var(--azure);}
  .txt{font-family:"Poppins",sans-serif;fill:var(--white);}
  .txt-strong{font-weight:500;}
  .txt-olive{fill:var(--olive);}
  .bullet{fill:#e23b3b;}
  .rule{stroke:var(--olive);stroke-width:2.5;}
  .rule-thin{stroke:#9fd6f0;stroke-width:0.8;}
  .dieline-label{font-family:"Poppins",sans-serif;font-weight:500;fill:var(--label);font-size:17px;}
</style>
</head>
<body>
<div class="canvas">
<svg viewBox="0 0 1500 1500" xmlns="http://www.w3.org/2000/svg">
  <defs>
    <linearGradient id="front-bg" x1="0" y1="0" x2="1" y2="1">
      <stop offset="0" stop-color="#1d4f9c"/>
      <stop offset="0.55" stop-color="#1f86c9"/>
      <stop offset="1" stop-color="#2bb6e6"/>
    </linearGradient>
    <linearGradient id="side-bg" x1="0" y1="0" x2="1" y2="0">
      <stop offset="0" stop-color="#2467b3"/>
      <stop offset="0.6" stop-color="#1f9bd8"/>
      <stop offset="1" stop-color="#2bb6e6"/>
    </linearGradient>
    <linearGradient id="photo-tone" x1="0" y1="0" x2="1" y2="1">
      <stop offset="0" stop-color="#5e6b78" stop-opacity="0.55"/>
      <stop offset="1" stop-color="#3e6e96" stop-opacity="0.85"/>
    </linearGradient>
    <linearGradient id="pad-tone" x1="0" y1="0" x2="0" y2="1">
      <stop offset="0" stop-color="#7c7f84"/>
      <stop offset="1" stop-color="#4a4d52"/>
    </linearGradient>

    <g id="box-dieline">
      <!-- top flaps -->
      <path class="flap" d="M697,125 L697,45 L705,37 L907,37 L915,48 L915,125 Z"/>
      <rect class="flap" x="690" y="125" width="230" height="92"/>
      <path class="flap" d="M603,217 L603,125 L613,115 L673,115 L681,125 L681,217 Z"/>
      <path class="flap" d="M932,217 L932,125 L942,115 L998,115 L1006,125 L1006,217 Z"/>
      <path class="flap" d="M1015,217 L1042,138 L1216,138 L1232,217 Z"/>
      <text class="brand-mark" x="712" y="166" font-size="30">HBP</text>
      <text class="brand-city" x="724" y="178" font-size="7">Busan Korea</text>

      <!-- glue flap -->
      <path class="flap" d="M1250,225 L1322,230 L1322,562 L1250,568 Z"/>

      <!-- bottom flaps -->
      <path class="flap" d="M693,668 L912,668 L912,750 L700,750 L693,742 Z"/>
      <path class="flap" d="M603,571 L681,571 L681,664 L673,672 L613,672 L603,662 Z"/>
      <path class="flap" d="M930,571 L1006,571 L1006,662 L998,672 L940,672 L930,662 Z"/>
      <path class="flap" d="M1015,571 L1232,571 L1216,650 L1042,650 Z"/>

      <!-- bottom inner panel (printed) -->
      <rect x="688" y="571" width="232" height="97" fill="url(#side-bg)"/>
      <rect class="panel-navy" x="829" y="617" width="78" height="51"/>
      <g transform="rotate(180 868 610)">
        <text class="txt" x="830" y="613" font-size="7">Hyemin Brake Pads</text>
        <line class="rule" x1="830" y1="616" x2="906" y2="616"/>
      </g>
      <text class="brand-mark" x="848" y="640" font-size="16" transform="rotate(180 866 634)">HBP</text>

      <!-- left side panel -->
      <rect x="573" y="217" width="117" height="354" fill="url(#side-bg)"/>
      <polygon class="stripe" points="612,217 628,217 690,330 690,365"/>
      <polygon points="630,217 690,217 690,320" fill="#2bb6e6" opacity="0.6"/>
      <rect x="623" y="232" width="52" height="102" rx="14" fill="url(#pad-tone)" role="img" aria-label="Brake pad product photo"/>
      <path d="M578,357 L603,357 L603,410 L578,410 Z" fill="none" stroke="#5aa9dc" stroke-width="1"/>
      <rect class="panel-navy" x="604" y="452" width="53" height="88"/>
      <text class="brand-mark" font-size="18" transform="translate(632,520) rotate(-90)">HBP</text>
      <text class="txt" font-size="8" transform="translate(654,540) rotate(-90)">Hyemin Brake Pads</text>

      <!-- back panel -->
      <rect class="panel-navy" x="690" y="217" width="230" height="354"/>
      <text class="brand-mark" x="711" y="268" font-size="32">HBP</text>
      <text class="brand-city" x="724" y="279" font-size="7">Busan Korea</text>
      <text class="txt txt-strong" x="710" y="304" font-size="10">Hyemin Brake Pads</text>
      <line class="rule" x1="710" y1="310" x2="818" y2="307"/>
      <text class="txt txt-strong" x="710" y="345" font-size="5.5">Disc Brake Pads</text>
      <text class="txt" x="710" y="361" font-size="6">100% Asbestos Free</text>
      <text class="txt" x="710" y="379" font-size="6">Limited Warranty</text>
      <text class="txt" x="710" y="387" font-size="6">(See Retailer for Details)</text>
      <polygon class="bullet" points="705,397 708,399 705,401"/>
      <text class="txt" x="710" y="401" font-size="5.5">Reduced noise with shims where applicable</text>
      <polygon class="bullet" points="705,408 708,410 705,412"/>
      <text class="txt" x="710" y="412" font-size="5.5">Extended wear life and quieter operation high tech-</text>
      <text class="txt" x="710" y="420" font-size="5.5">nology manufacturing</text>
      <polygon class="bullet" points="705,427 708,429 705,431"/>
      <text class="txt" x="710" y="431" font-size="5.5">Consistent braking performance throughout the life</text>
      <text class="txt" x="710" y="439" font-size="5.5">of the pads</text>
      <rect x="690" y="440" width="230" height="131" fill="url(#photo-tone)" role="img" aria-label="Close-up photo of ceramic brake pads"/>
      <text class="brand-mark" x="843" y="503" font-size="22">HBP</text>
      <text class="brand-city" x="853" y="512" font-size="5">Busan Korea</text>
      <text class="txt" x="844" y="522" font-size="5">Hyemin Brake Pads</text>
      <text class="txt" x="844" y="533" font-size="4.5">info@qe-roadspares.net</text>
      <text class="txt" x="844" y="540" font-size="4.5">Busan, Korea</text>

      <!-- right side panel -->
      <rect class="panel-sky" x="920" y="217" width="90" height="354"/>
      <polygon class="stripe" points="920,425 940,470 1000,571 975,571 920,470"/>
      <rect class="panel-navy" x="965" y="228" width="43" height="92"/>
      <text class="brand-mark" font-size="17" transform="translate(992,305) rotate(90)" text-anchor="end">HBP</text>
      <text class="txt" font-size="7.5" fill="#0b2660" transform="translate(952,232) rotate(90)" style="fill:var(--navy)">Hyemin Brake Pads</text>
      <rect x="938" y="448" width="48" height="105" rx="14" fill="url(#pad-tone)" role="img" aria-label="Brake pad product photo"/>

      <!-- front panel -->
      <rect x="1010" y="217" width="240" height="354" fill="url(#front-bg)"/>
      <polygon points="1250,300 1250,571 1120,571" fill="#2bb6e6" opacity="0.55"/>
      <polygon class="stripe" points="1250,420 1250,450 1160,571 1135,571"/>
      <polygon class="stripe" points="1250,480 1250,500 1200,571 1185,571" opacity="0.9"/>
      <rect class="panel-navy" x="1023" y="217" width="117" height="51"/>
      <text class="brand-mark" x="1047" y="256" font-size="28">HBP</text>
      <text class="brand-city" x="1060" y="266" font-size="6.5">Busan Korea</text>
      <line class="rule" x1="1022" y1="296" x2="1186" y2="298"/>
      <text class="txt txt-strong" x="1026" y="331" font-size="16">Professional</text>
      <line class="rule" x1="1026" y1="336" x2="1122" y2="336"/>
      <text class="txt txt-strong" x="1026" y="360" font-size="12">Disk brake pads</text>
      <text class="txt" x="1026" y="369" font-size="7.5">100% Asbestos free</text>
      <line class="rule-thin" x1="1026" y1="372" x2="1127" y2="372"/>
      <text class="txt txt-strong" x="1026" y="388" font-size="7">Plaquettes de freins a' disque</text>
      <text class="txt" x="1026" y="396" font-size="7.5">100% sans amiante</text>
      <line class="rule-thin" x1="1026" y1="399" x2="1127" y2="399"/>
      <text class="txt txt-olive" x="1026" y="428" font-size="15">Ceramic</text>
      <rect x="1010" y="440" width="240" height="131" fill="url(#photo-tone)" role="img" aria-label="Photo of two ceramic brake pads"/>
    </g>
  </defs>

  <!-- AW-1: brake pads -->
  <use href="#box-dieline"/>
  <text class="txt txt-strong" x="1022" y="289" font-size="15">Hyemin Brake Pads</text>
  <text class="dieline-label" x="946" y="694">AW-1</text>

  <!-- AW-2: brake shoes -->
  <g transform="translate(-540,550)">
    <use href="#box-dieline"/>
    <text class="txt txt-strong" x="1022" y="289" font-size="15">Hyemin Brake Shoes</text>
    <text class="dieline-label" x="945" y="696">AW-2</text>
  </g>
</svg>
</div>
</body>
</html>
```